CPA Firm Stationary & Business Cards
Whitfield & Partners CPAs PSC
CPA Firm Stationary & Business Cards - Financial Services
Creative Brief
Professional
Martin L. Dowse, CPA
Shareholder
4815 Tillamore Ave. Suite 1 Harlan Falls, KY 40999
mdowse@wpfcpa.net
www.wpfcpa.net
We are a CPA (Certified Public Accountant) firm, in business since 1924. In addition to Business Cards, I would also like to see designs for Letterheads and Envelopes.
Your choice. At a minimum, it should include the "W" logo.In addition to Business Cards, I would also like to see designs for Letterheads and Envelopes.

```html
<!DOCTYPE html>
<html lang="en">
<head>
<meta charset="utf-8">
<title>Whitfield &amp; Partners CPAs PSC — Business Card</title>
<link href="https://fonts.googleapis.com/css2?family=Michroma&display=swap" rel="stylesheet">
<style>
  :root {
    --backdrop: #e6e4e0;
    --card-white: #ffffff;
    --card-shade: #eeeff1;
    --brand-blue: #2f5fc9;
    --brand-deep: #1f3f9e;
    --band-grey: #a9acb2;
    --text-grey: #8a8d93;
  }
  * { margin: 0; padding: 0; box-sizing: border-box; }
  html, body { width: 1200px; height: 914px; overflow: hidden; }
  body {
    background: var(--backdrop);
    font-family: "Michroma", "Helvetica Neue", Arial, sans-serif;
    position: relative;
  }
  .business-card {
    position: absolute;
    left: 75px; top: 157px;
    width: 1050px; height: 600px;
    background: linear-gradient(160deg, var(--card-white) 40%, var(--card-shade) 100%);
    box-shadow: 0 6px 24px rgba(0,0,0,0.12);
    overflow: hidden;
  }
  .brand {
    position: absolute;
    left: 0; right: 0; top: 84px;
    display: flex; justify-content: center; align-items: center; gap: 22px;
  }
  .brand-dot {
    width: 74px; height: 74px; border-radius: 50%;
    background: var(--brand-blue);
    flex: none;
  }
  .brand-name {
    color: var(--brand-blue);
    font-weight: 400;
    line-height: 1.05;
  }
  .brand-name .primary { display: block; font-size: 42px; letter-spacing: 1px; text-transform: uppercase; }
  .brand-name .secondary { display: block; font-size: 20px; letter-spacing: 1px; text-transform: uppercase; }
  .person {
    position: absolute; left: 0; right: 0; top: 232px;
    text-align: center;
  }
  .person-name {
    color: var(--brand-blue);
    font-size: 19px; letter-spacing: 3px;
    font-variant: small-caps;
  }
  .person-title {
    margin-top: 8px;
    color: var(--text-grey);
    font-size: 14px; letter-spacing: 3px;
    font-variant: small-caps;
  }
  .address {
    position: absolute; right: 560px; top: 340px;
    text-align: right;
    color: var(--text-grey);
    font-style: normal;
    font-size: 12px; letter-spacing: 1.5px; line-height: 1.9;
    text-transform: uppercase;
    white-space: nowrap;
  }
  .contact-list {
    position: absolute; left: 520px; top: 322px;
    list-style: none;
    color: var(--text-grey);
    font-size: 12px; letter-spacing: 1.5px;
  }
  .contact-list li { display: flex; align-items: center; gap: 12px; height: 27px; white-space: nowrap; }
  .contact-icon {
    width: 18px; height: 18px; border-radius: 50%;
    background: var(--brand-blue);
    display: flex; align-items: center; justify-content: center;
    flex: none;
  }
  .card-band { position: absolute; left: 0; bottom: 0; width: 1050px; height: 150px; }
</style>
</head>
<body>
  <main class="business-card">
    <div class="brand">
      <span class="brand-dot"></span>
      <div class="brand-name">
        <span class="primary">Whitfield</span>
        <span class="secondary">&amp; Partners CPAs PSC</span>
      </div>
    </div>

    <div class="person">
      <p class="person-name">Martin L. Dowse, CPA</p>
      <p class="person-title">Shareholder</p>
    </div>

    <address class="address">
      4815 Tillamore Ave. Suite 6<br>
      Harlan Falls, KY 40999
    </address>

    <ul class="contact-list">
      <li><span class="contact-icon"><svg width="10" height="10" viewBox="0 0 10 10"><path d="M2 1 L4 1 L4.6 3 L3.4 4 Q4.5 6 6 6.6 L7 5.4 L9 6 L9 8 Q5 9 1.5 4.5 Q1 2.5 2 1Z" fill="#fff"/></svg></span>270-555-0148</li>
      <li><span class="contact-icon"><svg width="10" height="10" viewBox="0 0 10 10"><rect x="2" y="1" width="6" height="3" fill="#fff"/><rect x="1" y="4" width="8" height="4" fill="#fff"/></svg></span>270-555-0149</li>
      <li><span class="contact-icon"><svg width="10" height="10" viewBox="0 0 10 10"><rect x="1" y="2.5" width="8" height="5.5" fill="#fff"/><path d="M1 2.5 L5 5.5 L9 2.5" stroke="#2f5fc9" stroke-width="0.8" fill="none"/></svg></span>mdowse@wpfcpa.net</li>
      <li><span class="contact-icon"><svg width="10" height="10" viewBox="0 0 10 10"><circle cx="5" cy="5" r="3.8" fill="none" stroke="#fff" stroke-width="1"/><path d="M1.2 5 H8.8 M5 1.2 Q2.8 5 5 8.8 M5 1.2 Q7.2 5 5 8.8" stroke="#fff" stroke-width="0.8" fill="none"/></svg></span>www.wpfcpa.net</li>
    </ul>

    <svg class="card-band" viewBox="0 0 1050 150" preserveAspectRatio="none" aria-hidden="true">
      <defs>
        <linearGradient id="blueBand" x1="0" y1="0" x2="1" y2="0">
          <stop offset="0" stop-color="#1f3f9e"/>
          <stop offset="0.6" stop-color="#3a6fe0"/>
          <stop offset="1" stop-color="#2f5fc9"/>
        </linearGradient>
        <linearGradient id="greyBand" x1="0" y1="0" x2="1" y2="0">
          <stop offset="0" stop-color="#9a9da4"/>
          <stop offset="1" stop-color="#c3c5ca"/>
        </linearGradient>
      </defs>
      <path d="M0 40 L560 70 L600 150 L0 150 Z" fill="url(#blueBand)"/>
      <path d="M560 70 L1050 96 L1050 150 L600 150 Z" fill="url(#greyBand)"/>
    </svg>
  </main>
</body>
</html>
```